Marlowe Bay Consulting Business Card

Hi Corvel. Thank you for your work on my coaching business card. I have another business which needs a new card. It is my counselling business. The best way to find out how to approach this project will be to go to my other website. www.marlowebayconsulting.com.au and you will be able to see the colours scheme that I will require. White, Green and blue.

The tag line is Marlowe Bay Consulting So you can look forward to tomorrow. The clients are varied but mostly middle class Australian. The card is to show on it the same details as my other business card but with a different phone number. The tag lines are obviously different. The phone number is 9137 5264 The addresses are all the same.

Again simple, professional sophisticated is best.

```html
<!DOCTYPE html>
<html lang="en">
<head>
<meta charset="utf-8">
<title>Marlowe Bay Consulting Business Card</title>
<link rel="stylesheet" href="https://fonts.googleapis.com/css2?family=Montserrat:wght@300;400&family=Arimo:wght@400&display=swap">
<style>
  :root {
    --backdrop: #e9e7e3;
    --card-blue: #4585cc;
    --card-white: #ffffff;
    --accent-green: #8cc63f;
    --ink: #1e1e1e;
    --ink-soft: #444444;
    --front-text: #f4f6fa;
  }
  * { box-sizing: border-box; margin: 0; padding: 0; }
  html, body { width: 1200px; height: 803px; overflow: hidden; }
  body {
    background: var(--backdrop);
    display: flex;
    align-items: center;
    justify-content: center;
    gap: 50px;
    font-family: "Arimo", Arial, sans-serif;
  }
  .card {
    width: 540px;
    height: 310px;
    position: relative;
    box-shadow: 0 6px 18px rgba(0,0,0,0.18);
  }

  /* Front */
  .card--front {
    background: var(--card-blue);
    color: var(--front-text);
    padding: 84px 34px 0 34px;
  }
  .front__name {
    font-family: "Montserrat", Arial, sans-serif;
    font-weight: 400;
    font-size: 34px;
    line-height: 1;
    white-space: nowrap;
  }
  .front__tagline {
    font-family: "Montserrat", Arial, sans-serif;
    font-weight: 300;
    font-size: 14px;
    letter-spacing: 1.4px;
    text-transform: uppercase;
    white-space: nowrap;
    margin-top: 16px;
  }
  .front__services {
    list-style: none;
    margin-top: 22px;
    font-family: "Montserrat", Arial, sans-serif;
    font-weight: 400;
    font-size: 11px;
    letter-spacing: 1px;
    text-transform: uppercase;
    line-height: 1.6;
    white-space: nowrap;
  }
  .front__services .dot { color: var(--accent-green); padding: 0 4px; }

  /* Back */
  .card--back {
    background: var(--card-white);
    padding: 34px 28px 0 30px;
    color: var(--ink);
  }
  .back__header {
    display: flex;
    justify-content: space-between;
    align-items: flex-end;
  }
  .back__brand-name {
    font-family: "Montserrat", Arial, sans-serif;
    font-weight: 400;
    font-size: 19px;
    color: var(--ink);
    line-height: 1;
    white-space: nowrap;
  }
  .back__brand-tagline {
    font-family: "Montserrat", Arial, sans-serif;
    font-size: 9px;
    letter-spacing: 0.8px;
    color: var(--ink-soft);
    text-transform: uppercase;
    margin-top: 6px;
    white-space: nowrap;
  }
  .back__person {
    font-family: "Montserrat", Arial, sans-serif;
    font-size: 24px;
    font-weight: 400;
    line-height: 1;
    padding-bottom: 1px;
    white-space: nowrap;
  }
  .back__rule {
    height: 2px;
    background: var(--accent-green);
    margin: 9px 0 5px;
  }
  .back__role {
    text-align: right;
    font-size: 11px;
    color: var(--ink-soft);
  }
  .back__contacts {
    list-style: none;
    margin-top: 26px;
    font-size: 12.5px;
    line-height: 1.5;
  }
  .back__contacts li { display: flex; align-items: center; gap: 8px; }
  .back__contacts svg { width: 12px; height: 12px; fill: var(--ink); flex: none; }
  .back__offices {
    list-style: none;
    margin-top: 14px;
    font-size: 11.5px;
    line-height: 1.55;
    white-space: nowrap;
  }
</style>
</head>
<body>

<section class="card card--front" aria-label="Card front">
  <h1 class="front__name">Marlowe Bay Consulting</h1>
  <p class="front__tagline">So you can look forward to tomorrow</p>
  <ul class="front__services">
    <li>Relationships Counselling <span class="dot">&#9679;</span> Drug and Alcohol Counselling</li>
    <li>Confidence Coaching <span class="dot">&#9679;</span> Life Coaching <span class="dot">&#9679;</span> Executive Coaching</li>
  </ul>
</section>

<section class="card card--back" aria-label="Card back">
  <div class="back__header">
    <div class="back__brand">
      <div class="back__brand-name">Marlowe Bay Consulting</div>
      <div class="back__brand-tagline">So you can look forward to tomorrow</div>
    </div>
    <div class="back__person">Tom Hadley</div>
  </div>
  <div class="back__rule"></div>
  <p class="back__role">Clinical Psychotherapist and Executive Coach</p>

  <ul class="back__contacts">
    <li>
      <svg viewBox="0 0 12 12" aria-hidden="true"><path d="M2.5 1 4.5 1 5.2 3.6 4 4.6C4.7 6 6 7.3 7.4 8L8.4 6.8 11 7.5 11 9.5C11 10.3 10.3 11 9.5 11 5 11 1 7 1 2.5 1 1.7 1.7 1 2.5 1Z"/></svg>
      +612 9137 5264
    </li>
    <li>
      <svg viewBox="0 0 12 12" aria-hidden="true"><rect x="0.5" y="2" width="11" height="8" rx="1"/><path d="M1 2.8 6 6.6 11 2.8" stroke="#fff" stroke-width="1" fill="none"/></svg>
      info@marlowebayconsulting.com.au
    </li>
    <li>
      <svg viewBox="0 0 12 12" aria-hidden="true"><circle cx="6" cy="6" r="5.5"/><path d="M0.5 6H11.5M6 0.5C3.5 3 3.5 9 6 11.5M6 0.5C8.5 3 8.5 9 6 11.5" stroke="#fff" stroke-width="0.8" fill="none"/></svg>
      www.marlowebayconsulting.com.au
    </li>
  </ul>

  <ul class="back__offices">
    <li>Harbourside Office: 48 Wattle Point Road Ashby NSW 2981</li>
    <li>Northgate Office: Suite 3 / 27 Linden Street Northgate NSW 2984</li>
    <li>Kingsway Office: Suite 12 / 309 Kingsway Street Ashby CBD NSW 2987</li>
  </ul>
</section>

</body>
</html>
```